Food truck menu design

Looking for a menu to be dissed for my toasted sandwich food truck. I have attached to logo and photo of the food truck for inspiration. if it can tie into them.
needing three sections, with titles:
CLASSICS
- classic one
. description
-Classic two
. Description
PREMIUM
- Premium one
. description
-Premium Two
. Description
-Premium Three
. Description
DESERT
-Desert one
. Description
-Desert two
.Description

also if it can be editable so I can change menu items and descriptions.

```html
<!DOCTYPE html>
<html lang="en">
<head>
<meta charset="utf-8">
<title>Mako's Melts – Toasted Sandwich Food Truck Menu</title>
<link rel="stylesheet" href="https://fonts.googleapis.com/css2?family=Kaushan+Script&family=Montserrat:wght@700;800;900&family=Poppins:wght@400;600;700&display=swap">
<style>
  :root {
    --page-bg: #e6e6e6;
    --white: #ffffff;
    --brown: #4a1a10;
    --red: #b5393b;
    --orange: #f29a1e;
    --orange-deep: #f07f10;
    --yellow: #ffd200;
    --tan: #e0891a;
  }
  * { box-sizing: border-box; margin: 0; padding: 0; }
  html, body { width: 800px; height: 1200px; overflow: hidden; }
  body { background: var(--page-bg); position: relative; font-family: "Poppins", sans-serif; }

  .menu-board {
    position: absolute; left: 20px; top: 221px;
    width: 760px; height: 758px;
    background: var(--white); overflow: hidden;
  }
  .sunburst {
    position: absolute; left: 0; top: 0; width: 760px; height: 410px;
    background:
      repeating-conic-gradient(from 0deg at 343px 322px, rgba(255,255,255,0.09) 0deg 6deg, rgba(255,255,255,0) 6deg 12deg),
      radial-gradient(circle at 343px 322px, var(--yellow) 0%, #ffb300 40%, var(--orange-deep) 90%);
  }
  .torn-edge { position: absolute; left: 0; top: 396px; width: 760px; height: 20px; }

  .brand-tab {
    position: absolute; left: 36px; top: 0; width: 180px; height: 181px;
    background: var(--white);
    border-radius: 0 0 90px 90px;
    border-bottom: 5px solid var(--brown);
    display: flex; flex-direction: column; align-items: center; justify-content: center; gap: 8px;
    padding-top: 10px;
  }
  .brand-dot { width: 30px; height: 30px; border-radius: 50%; background: var(--orange); }
  .brand-name { font-family: "Montserrat", sans-serif; font-weight: 800; font-size: 21px; color: var(--brown); }

  .headline-script {
    position: absolute; left: 236px; top: 24px;
    font-family: "Kaushan Script", cursive; font-size: 86px; line-height: 1; color: var(--brown);
  }
  .speed-lines { position: absolute; left: 540px; top: 58px; width: 56px; height: 60px; }
  .headline-main {
    position: absolute; left: 236px; top: 128px;
    font-family: "Montserrat", sans-serif; font-weight: 900; font-size: 69px; line-height: 1;
    letter-spacing: -1px; color: var(--brown);
  }
  .headline-sub {
    position: absolute; left: 240px; top: 198px;
    font-family: "Montserrat", sans-serif; font-weight: 800; font-size: 49px; line-height: 1;
    color: var(--red);
  }
  .truck-icon { position: absolute; left: 586px; top: 202px; width: 80px; height: 44px; }

  .deco-sandwich { position: absolute; background: var(--tan); border-radius: 10px; opacity: 0.85; }
  .deco-left { left: 73px; top: 207px; width: 81px; height: 78px; }
  .deco-right { left: 551px; top: 281px; width: 74px; height: 70px; }

  .dashed-path { position: absolute; left: 100px; top: 285px; width: 110px; height: 125px; }

  .photo-sandwich {
    position: absolute; left: 107px; top: 263px; width: 400px; height: 220px;
    border-radius: 30px 30px 120px 120px;
    background: linear-gradient(180deg, #e8c592 0%, #d69a55 45%, #7fb04a 70%, #f3f3f3 100%);
  }
  .photo-dessert {
    position: absolute; left: 510px; top: 366px; width: 192px; height: 117px;
    border-radius: 60px 60px 40px 40px;
    background: linear-gradient(180deg, #eeeaea 0%, #c89a6a 60%, #b98347 100%);
  }

  .menu-sections { position: absolute; left: 31px; top: 500px; width: 700px; height: 204px; }
  .menu-card { position: absolute; top: 0; width: 221px; height: 204px; }
  .menu-card.classics { left: 0; }
  .menu-card.premium { left: 240px; }
  .menu-card.dessert { left: 480px; }
  .card-body {
    position: absolute; left: 0; top: 19px; width: 221px; height: 185px;
    border-radius: 12px; background: var(--red);
  }
  .premium .card-body { background: var(--brown); }
  .card-body::after {
    content: ""; position: absolute; inset: 7px;
    border: 1.5px dashed rgba(255,255,255,0.85); border-radius: 8px;
  }
  .card-title {
    position: absolute; left: 19px; top: 0; width: 183px; height: 36px;
    background: var(--orange);
    clip-path: polygon(0 0, 100% 0, 94% 100%, 6% 100%);
    display: flex; align-items: center; justify-content: center;
    font-family: "Montserrat", sans-serif; font-weight: 800; font-size: 16px; color: var(--white);
    z-index: 2;
  }
  .menu-items { position: absolute; left: 16px; top: 26px; width: 189px; z-index: 1; }
  .menu-item + .menu-item { margin-top: 6px; }
  .item-head {
    display: flex; justify-content: space-between;
    font-family: "Montserrat", sans-serif; font-weight: 800; font-size: 12px; line-height: 15px; color: var(--white);
  }
  .item-desc { font-size: 8.8px; line-height: 11px; color: var(--white); margin-top: 1px; }

  .web-address {
    position: absolute; left: 0; top: 714px; width: 760px; text-align: center;
    font-family: "Poppins", sans-serif; font-weight: 700; font-size: 16px; letter-spacing: 3px; color: var(--brown);
  }
  .web-address span { color: var(--red); }
  .base-band { position: absolute; left: 0; bottom: 0; width: 760px; height: 11px; background: var(--brown); }
</style>
</head>
<body>
  <main class="menu-board">
    <div class="sunburst"></div>
    <svg class="torn-edge" viewBox="0 0 760 20" preserveAspectRatio="none">
      <path d="M0 10 L40 6 L80 12 L120 5 L160 11 L200 7 L240 13 L280 6 L320 10 L360 5 L400 12 L440 7 L480 11 L520 5 L560 12 L600 6 L640 10 L680 5 L720 11 L760 7 L760 20 L0 20 Z" fill="#ffffff"/>
    </svg>

    <div class="brand-tab">
      <div class="brand-dot"></div>
      <div class="brand-name">Mako's Melts</div>
    </div>

    <h1 class="headline-script">Toasted</h1>
    <svg class="speed-lines" viewBox="0 0 56 60">
      <g stroke="#c0392b" stroke-width="5" stroke-linecap="round" fill="none">
        <line x1="30" y1="8" x2="8" y2="20"/>
        <line x1="10" y1="30" x2="52" y2="30"/>
        <line x1="8" y1="40" x2="30" y2="52"/>
      </g>
    </svg>
    <h2 class="headline-main">SANDWICH</h2>
    <h3 class="headline-sub">FOOD TRUCK</h3>
    <svg class="truck-icon" viewBox="0 0 80 44" fill="none" stroke="#b5393b" stroke-width="2.5" stroke-linejoin="round">
      <line x1="2" y1="30" x2="12" y2="30"/>
      <line x1="6" y1="36" x2="14" y2="36"/>
      <rect x="16" y="4" width="40" height="30" rx="3"/>
      <rect x="22" y="12" width="28" height="8"/>
      <path d="M56 14 H68 L77 26 V34 H56 Z"/>
      <circle cx="28" cy="36" r="5" fill="#ffc400"/>
      <circle cx="66" cy="36" r="5" fill="#ffc400"/>
    </svg>

    <div class="deco-sandwich deco-left" role="img" aria-label="Small toasted sandwich triangle graphic"></div>
    <div class="deco-sandwich deco-right" role="img" aria-label="Small toasted sandwich triangle graphic"></div>

    <svg class="dashed-path" viewBox="0 0 110 125" fill="none">
      <path d="M7 120 C5 60 40 15 100 8" stroke="#4a1a10" stroke-width="2.5" stroke-dasharray="9 6"/>
    </svg>

    <div class="photo-sandwich" role="img" aria-label="Photo of a stacked toasted sandwich with lettuce, tomato and cheese on a white plate, with a small dish of ketchup"></div>
    <div class="photo-dessert" role="img" aria-label="Photo of ice cream with chocolate and berry sauce in a waffle bowl with a strawberry"></div>

    <section class="menu-sections">
      <article class="menu-card classics">
        <h4 class="card-title">CLASSICS</h4>
        <div class="card-body">
          <div class="menu-items">
            <div class="menu-item">
              <div class="item-head"><span>CLASSIC ONE</span><span>$10</span></div>
              <p class="item-desc">Lorem Ipsum is simply dummy text of the printing and typesetting industry.</p>
            </div>
            <div class="menu-item">
              <div class="item-head"><span>CLASSIC TWO</span><span>$12</span></div>
              <p class="item-desc">Lorem Ipsum is simply dummy text of the printing and typesetting industry. Lorem Ipsum has been the industry's standard dummy.</p>
            </div>
          </div>
        </div>
      </article>

      <article class="menu-card premium">
        <h4 class="card-title">PREMIUM</h4>
        <div class="card-body">
          <div class="menu-items">
            <div class="menu-item">
              <div class="item-head"><span>PREMIUM ONE</span><span>$15</span></div>
              <p class="item-desc">Lorem Ipsum is simply dummy text of the printing and typesetting industry.</p>
            </div>
            <div class="menu-item">
              <div class="item-head"><span>PREMIUM TWO</span><span>$16</span></div>
              <p class="item-desc">Lorem Ipsum is simply dummy text of the printing and typesetting industry. Lorem Ipsum has been the industry's standard dummy.</p>
            </div>
            <div class="menu-item">
              <div class="item-head"><span>PREMIUM THREE</span><span>$17</span></div>
              <p class="item-desc">Lorem Ipsum is simply dummy text of the printing and typesetting industry.</p>
            </div>
          </div>
        </div>
      </article>

      <article class="menu-card dessert">
        <h4 class="card-title">DESERT</h4>
        <div class="card-body">
          <div class="menu-items">
            <div class="menu-item">
              <div class="item-head"><span>CLASSIC ONE</span><span>$10</span></div>
              <p class="item-desc">Lorem Ipsum is simply dummy text of the printing and typesetting industry.</p>
            </div>
            <div class="menu-item">
              <div class="item-head"><span>CLASSIC TWO</span><span>$13</span></div>
              <p class="item-desc">Lorem Ipsum is simply dummy text of the printing and typesetting industry. Lorem Ipsum has been the industry's standard dummy.</p>
            </div>
          </div>
        </div>
      </article>
    </section>

    <p class="web-address">www.<span>makosmelts</span>.com</p>
    <div class="base-band"></div>
  </main>
</body>
</html>
```